Powerpoint Template needed for new Digital Consultancy

We have recently had our logo designed through Brushvale and would now like to extend the brand look & feel through to having a powerpoint template created that we can use as a master template within which to create our client presentations.
Typical slides required and in terms of what we would need templating is:

- Stylised header and footer for main content slides
- intro/front page slide
- contents page slide
- standardised font type and sizes, heading types (including sizes) for Level 1, Level 2 and Level 3 headings
- use of text colour and any standards/styling around when to use bold, underline, italics etc
- table styling for when we want to use tables in the presentation
- standards and styles around using bullet and number lists
- stylising use of imagery that is dropped in e.g. do all images have a certain border style or drop-shadow etc.
- style and slide layout/format for how team profiles are handled
- style and slide layout/format for how case studies are handled
- closing, contact-us page

We can send over logo files and colour/font styles etc used for the logo soon.

Target Market(s)

B2B professional clients that are either medium to large corporations or potentially some government departments.

Industry/Entity Type

Digital

Font styles to use
Sans Serif

Colors
ec1f27
f37122
f78f20
faa54b
f68d4d
0255a3

Requirements
Must have
• Ideally as many templated pages/master slide types as outlined above in the brief to meet the requirements of what the powerpoint deck will be used for. Namely client presentations and pitches.
• Versions of the logo are attached to give an idea of the colour palette and clean, modern style we are looking for, plus the type of font we are using and like.
• We are looking for the slide design to be modern, minimalistic, clean and not overuse of colour. Preferably a white slide background so it's easy to then read slide content when we populate the slides with text which will be in black.
Nice to have
• Not expecting to see too much more than simple use of the logo and a slide header perhaps using some sort of line as a break and then a simple footer as well.
• Consider using Abode font.
Should not have
• Too much block colour or elements that draw away from what will go in the main content body of our slides when we use them.

```html
<!DOCTYPE html>
<html lang="en">
<head>
<meta charset="utf-8">
<title>Orbitline Presentation Template</title>
<link rel="stylesheet" href="https://fonts.googleapis.com/css2?family=Open+Sans:ital,wght@0,300;0,400;0,600;1,400&display=swap">
<style>
  :root {
    --red: #ec1f27;
    --title: #e8452c;
    --orange: #f37122;
    --orange-light: #f9a35a;
    --peach: #f0c8a8;
    --rule: #f2a898;
    --blue-rule: #a9bfd8;
    --text: #555555;
    --muted: #8a8a8a;
    --panel: #f4f4f4;
    --divider: #222222;
    --white: #ffffff;
  }
  * { box-sizing: border-box; margin: 0; padding: 0; }
  html, body { width: 1200px; height: 918px; overflow: hidden; background: var(--white); }
  body { font-family: "Open Sans", Arial, sans-serif; color: var(--text); position: relative; }

  .divider-v { position: absolute; left: 603px; top: 0; width: 1px; height: 918px; background: var(--divider); }
  .divider-h { position: absolute; left: 0; top: 448px; width: 1200px; height: 1px; background: var(--divider); }

  .slide { position: absolute; }
  .abs { position: absolute; }

  /* header */
  .title-mark { position: absolute; width: 2px; height: 50px; background: var(--blue-rule); }
  .title-mark::after { content: ""; position: absolute; left: -5px; top: 18px; width: 12px; height: 12px; border-radius: 50%; border: 2px solid var(--orange); background: var(--white); }
  .slide-title { position: absolute; font-weight: 300; font-size: 25px; color: var(--title); line-height: 1; white-space: nowrap; }

  /* footer */
  .page-dot { position: absolute; width: 12px; height: 12px; border-radius: 50%; background: var(--red); color: var(--white); font-size: 6px; line-height: 12px; text-align: center; }
  .footer-rule { position: absolute; height: 1px; background: var(--rule); }
  .footer-rule::after { content: ""; position: absolute; right: -3px; top: -2.5px; width: 6px; height: 6px; border-radius: 50%; background: var(--red); }
  .brand { position: absolute; display: flex; align-items: center; gap: 6px; font-size: 15px; font-weight: 600; color: var(--orange); white-space: nowrap; }
  .brand-dot { width: 14px; height: 14px; border-radius: 50%; border: 2px solid var(--orange); }

  /* table */
  .data-table { position: absolute; left: 29px; top: 156px; width: 534px; border-collapse: collapse; font-size: 6.5px; color: #444; }
  .data-table th { height: 18px; text-align: left; font-weight: 600; color: var(--white); background: var(--orange); padding-left: 9px; }
  .data-table th.col-answer { background: var(--orange-light); }
  .data-table td { height: 15.3px; border-bottom: 1px solid #f1e6de; padding-left: 9px; }
  .data-table .col-text { width: 409px; }
  .data-table .col-yes { width: 62px; }

  /* case study */
  .image-panel { background: var(--panel); }
  .case-label { position: absolute; left: 698px; width: 93px; text-align: center; font-size: 19px; line-height: 26px; color: var(--orange); }
  .thin-rule { position: absolute; height: 1px; background: #c9c9c9; }
  .accent-bar { position: absolute; left: 817px; top: 178px; width: 3px; height: 109px; background: var(--orange); }
  .case-box { position: absolute; left: 820px; top: 144px; width: 300px; height: 174px; border: 1px solid var(--peach); border-radius: 18px; }
  .case-list { position: absolute; left: 855px; top: 166px; width: 250px; list-style: disc; font-size: 11px; line-height: 22px; color: var(--text); padding-left: 18px; }

  /* two content */
  .col-heading { position: absolute; width: 180px; text-align: center; font-size: 13px; color: var(--orange); }
  .col-rule { position: absolute; height: 1px; background: var(--blue-rule); top: 659px; }
  .icon-badge { position: absolute; width: 68px; height: 68px; border-radius: 50%; background: #f1f1f1; display: flex; align-items: center; justify-content: center; }
  .icon-badge span { width: 56px; height: 56px; border-radius: 50%; background: var(--orange); display: flex; align-items: center; justify-content: center; }
  .col-body { position: absolute; top: 704px; width: 248px; font-size: 11px; line-height: 15.3px; color: var(--text); }
  .col-body em { font-style: normal; color: var(--orange); }

  /* section header */
  .section-slide { left: 607px; top: 516px; width: 593px; height: 375px; background: var(--red); }
  .section-circle { position: absolute; left: 225px; top: 52px; width: 142px; height: 142px; border-radius: 50%; background: #f2f2f2; display: flex; align-items: center; justify-content: center; }
  .section-title { position: absolute; left: 0; top: 202px; width: 593px; text-align: center; color: var(--white); font-size: 19px; font-weight: 600; letter-spacing: 0.2px; }
  .section-rule { position: absolute; left: 62px; top: 241px; width: 470px; border-top: 1px dotted rgba(255,255,255,0.55); }
  .section-text { position: absolute; left: 80px; top: 252px; width: 433px; text-align: center; color: var(--white); font-size: 10px; font-style: italic; line-height: 16px; }
</style>
</head>
<body>
  <div class="divider-v"></div>
  <div class="divider-h"></div>

  <!-- Table slide -->
  <section class="slide-table">
    <div class="title-mark" style="left:25px; top:81px;"></div>
    <h1 class="slide-title" style="left:46px; top:93px;">Table Slide</h1>
    <table class="data-table">
      <thead>
        <tr><th class="col-text">Lorem ipsum</th><th class="col-answer" colspan="2">Lorem ipsum</th></tr>
      </thead>
      <tbody>
        <tr><td class="col-text">Lorem ipsum dolor sit amet, consectetur adipiscing elit</td><td class="col-yes">Yes</td><td>No</td></tr>
        <tr><td class="col-text">Lorem ipsum dolor sit amet, consectetur adipiscing elit</td><td class="col-yes">Yes</td><td>No</td></tr>
        <tr><td class="col-text">Lorem ipsum dolor sit amet, consectetur adipiscing elit</td><td class="col-yes">Yes</td><td>No</td></tr>
        <tr><td class="col-text">Lorem ipsum dolor sit amet, consectetur adipiscing elit</td><td class="col-yes">Yes</td><td>No</td></tr>
        <tr><td class="col-text">Lorem ipsum dolor sit amet, consectetur adipiscing elit</td><td class="col-yes">Yes</td><td>No</td></tr>
        <tr><td class="col-text">Lorem ipsum dolor sit amet, consectetur adipiscing elit</td><td class="col-yes">Yes</td><td>No</td></tr>
        <tr><td class="col-text">Lorem ipsum dolor sit amet, consectetur adipiscing elit</td><td class="col-yes">Yes</td><td>No</td></tr>
        <tr><td class="col-text">Lorem ipsum dolor sit amet, consectetur adipiscing elit</td><td class="col-yes">Yes</td><td>No</td></tr>
        <tr><td class="col-text">Lorem ipsum dolor sit amet, consectetur adipiscing elit</td><td class="col-yes">Yes</td><td>No</td></tr>
      </tbody>
    </table>
    <div class="page-dot" style="left:18px; top:357px;">5</div>
    <div class="footer-rule" style="left:30px; top:363px; width:455px;"></div>
    <div class="brand" style="left:492px; top:352px;"><span class="brand-dot"></span>Orbitline</div>
  </section>

  <!-- Case study slide -->
  <section class="slide-case">
    <div class="title-mark" style="left:628px; top:81px;"></div>
    <h1 class="slide-title" style="left:653px; top:93px;">Case Study Slide</h1>
    <div class="abs image-panel" role="img" aria-label="Case study image placeholder" style="left:610px; top:163px; width:62px; height:140px;"></div>
    <svg class="abs" style="left:726px; top:150px;" width="36" height="46" viewBox="0 0 36 46" fill="none" stroke="#f37122" stroke-width="2" aria-hidden="true">
      <path d="M12 30c0-5-8-8-8-16a14 14 0 0 1 28 0c0 8-8 11-8 16z"/>
      <line x1="12" y1="35" x2="24" y2="35"/><line x1="13" y1="39" x2="23" y2="39"/><line x1="15" y1="43" x2="21" y2="43"/>
      <path d="M15 30v-8l3 3 3-3v8"/>
    </svg>
    <div class="thin-rule" style="left:698px; top:210px; width:93px;"></div>
    <div class="case-label" style="top:218px;">Lorem<br>Ipsum</div>
    <div class="thin-rule" style="left:698px; top:279px; width:93px;"></div>
    <div class="accent-bar"></div>
    <div class="case-box"></div>
    <ul class="case-list">
      <li>Lorem ipsum dolor sit amet, consectetur adipiscing elit</li>
      <li>Lorem ipsum dolor sit amet, consectetur adipiscing elit</li>
      <li>Lorem ipsum dolor sit amet, consectetur adipiscing elit</li>
    </ul>
    <div class="page-dot" style="left:625px; top:357px;">6</div>
    <div class="footer-rule" style="left:637px; top:363px; width:454px;"></div>
    <div class="brand" style="left:1097px; top:352px;"><span class="brand-dot"></span>Orbitline</div>
  </section>

  <!-- Two content slide -->
  <section class="slide-two">
    <div class="title-mark" style="left:25px; top:549px;"></div>
    <h1 class="slide-title" style="left:46px; top:553px;">Two Content Slide</h1>

    <div class="col-heading" style="left:51px; top:605px;">Lorem ipsum</div>
    <div class="col-rule" style="left:51px; width:181px;"></div>
    <div class="icon-badge" style="left:107px; top:625px;"><span>
      <svg width="24" height="26" viewBox="0 0 24 26" fill="none" stroke="#fff" stroke-width="1.6" aria-hidden="true"><rect x="3" y="5" width="18" height="20"/><rect x="7" y="1" width="10" height="4"/><path d="M7 10h3M14 10h3M7 15h3M14 15h3M10 25v-5h4v5"/></svg>
    </span></div>
    <p class="col-body" style="left:46px;"><em>Lorem ipsum</em> dolor sit amet, consectetur adipiscing elit. Etiam ornare velit at sem euismod, ut pellentesque odio sodales. Ut id rutrum lacus. Phasellus in laoreet dolor. Sed ac nunc fermentum, varius sem vitae, bibendum dui.</p>

    <div class="col-heading" style="left:335px; top:605px;">Lorem ipsum</div>
    <div class="col-rule" style="left:335px; width:181px;"></div>
    <div class="icon-badge" style="left:391px; top:625px;"><span>
      <svg width="24" height="26" viewBox="0 0 24 26" fill="none" stroke="#fff" stroke-width="1.6" aria-hidden="true"><rect x="3" y="5" width="18" height="20"/><rect x="7" y="1" width="10" height="4"/><path d="M7 10h3M14 10h3M7 15h3M14 15h3M10 25v-5h4v5"/></svg>
    </span></div>
    <p class="col-body" style="left:304px;"><em>Lorem ipsum</em> dolor sit amet, consectetur adipiscing elit. Etiam ornare velit at sem euismod, ut pellentesque odio sodales. Ut id rutrum lacus. Phasellus in laoreet dolor. Sed ac nunc fermentum, varius sem vitae, bibendum dui.</p>

    <div class="page-dot" style="left:18px; top:817px;">7</div>
    <div class="footer-rule" style="left:30px; top:823px; width:455px;"></div>
    <div class="brand" style="left:492px; top:812px;"><span class="brand-dot"></span>Orbitline</div>
  </section>

  <!-- Section header slide -->
  <section class="slide section-slide">
    <div class="section-circle">
      <svg width="74" height="66" viewBox="0 0 74 66" fill="none" stroke="#ec1f27" stroke-width="2.2" aria-hidden="true">
        <circle cx="24" cy="42" r="14" stroke-dasharray="4.4 3"/>
        <circle cx="24" cy="42" r="10"/>
        <circle cx="24" cy="42" r="4"/>
        <circle cx="52" cy="20" r="11" stroke-dasharray="3.6 2.6"/>
        <circle cx="52" cy="20" r="7.5"/>
        <circle cx="52" cy="20" r="3"/>
      </svg>
    </div>
    <h2 class="section-title">SECTION HEADER</h2>
    <div class="section-rule"></div>
    <p class="section-text">Lorem ipsum dolor sit amet, consectetur adipiscing elit. Etiam ornare velit at sem euismod, ut pellentesque odio sodales</p>
  </section>
</body>
</html>
```